2013 Golf Outing Flyer

Our charitable organization was created in honor of my daughter who died at age 16. Our annual fundraiser is a golf tournament. I am not a creative person so I'd like someone to design a printable flyer that grabs people's attention but is not too busy while incorportating our organization's logo with the basic information.

Event details:
3rd Annual Marisol Quinn Dorsey Memorial Golf Tournament
4 person scramble

Saturday October 5th, 2013
Fernhollow Golf Club, Auburn, IL
9:30 Registration
Shotgun start at noon
To Register go online to www.marisolqdorseygolf.teeupsignups.example or email
marisoldorseyscholarship@mailbox.example

Scholarships to Cedar Ridge High School seniors are made possible by our orgnization through this fundraiser.
Updates

Target Market(s)

golfers and businesses willing to sponsor event

Industry/Entity Type

School

Requirements
Must have
• single page-easy to print
includes non profit organization logo which I attached (think I did)
Specific information about the tournament- date and location and registration info
Nice to have
• company logo and the golf outing logo but if both are too much, then just the golf logo and the organization name can be at the bottom

```html
<!DOCTYPE html>
<html lang="en">
<head>
<meta charset="utf-8">
<title>Marisol Quinn Dorsey Memorial Golf Tournament</title>
<link rel="stylesheet" href="https://fonts.googleapis.com/css2?family=Roboto+Condensed:wght@400;700&family=Open+Sans+Condensed:wght@300&display=swap">
<style>
  :root {
    --page: #ffffff;
    --sky-top: #6fa9cf;
    --sky-mid: #a9cde2;
    --cloud: #eef3ef;
    --haze: #d9e7dc;
    --tree: #3f7a3c;
    --fairway: #8cc04a;
    --fairway-deep: #2f6a2a;
    --title-blue: #3f6d8f;
    --info-blue: #2c4b68;
    --accent-orange: #ec7424;
    --footer-text: #ffffff;
  }
  * { margin: 0; padding: 0; box-sizing: border-box; }
  html, body {
    width: 852px; height: 1200px; overflow: hidden;
    background: var(--page);
  }
  .flyer {
    position: absolute; left: 40px; top: 50px;
    width: 772px; height: 1100px; overflow: hidden;
  }
  .scene { position: absolute; inset: 0; width: 100%; height: 100%; }
  .headline {
    position: absolute; right: 44px; top: 92px;
    text-align: right;
    font-family: "Roboto Condensed", "Arial Narrow", sans-serif;
    font-weight: 700;
    color: var(--title-blue);
  }
  .headline .edition { font-size: 28px; line-height: 30px; }
  .headline .edition sup { font-size: 16px; }
  .headline .honoree { font-size: 42px; line-height: 40px; }
  .headline .sport {
    color: var(--accent-orange); font-size: 150px; line-height: 122px;
    letter-spacing: -2px; margin-top: 6px;
  }
  .headline .event { color: var(--accent-orange); font-size: 42px; line-height: 40px; }
  .headline .format { font-size: 34px; line-height: 36px; }
  .schedule {
    position: absolute; right: 44px; top: 500px; text-align: right;
    font-family: "Roboto Condensed", "Arial Narrow", sans-serif;
    color: var(--title-blue);
  }
  .schedule .date { font-weight: 700; font-size: 46px; line-height: 44px; }
  .schedule .date sup { font-size: 24px; }
  .schedule .details {
    margin-top: 14px; font-size: 27px; line-height: 32px;
    color: var(--info-blue);
  }
  .fine-print {
    position: absolute; left: 0; right: 0; bottom: 54px;
    text-align: center;
    font-family: "Roboto Condensed", "Arial Narrow", sans-serif;
    font-size: 13px; line-height: 22px; color: var(--footer-text);
  }
</style>
</head>
<body>
  <main class="flyer">
    <svg class="scene" role="img" aria-label="Illustration of a golfer in a green shirt and brown trousers finishing his swing on a fairway, with blue sky, large white clouds and a line of dark trees" viewBox="0 0 772 1100" preserveAspectRatio="none">
      <defs>
        <linearGradient id="sky-to-course" x1="0" y1="0" x2="0" y2="1">
          <stop offset="0" stop-color="var(--sky-top)"/>
          <stop offset="0.22" stop-color="var(--sky-mid)"/>
          <stop offset="0.45" stop-color="var(--cloud)"/>
          <stop offset="0.72" stop-color="var(--haze)"/>
          <stop offset="0.80" stop-color="var(--tree)"/>
          <stop offset="0.86" stop-color="var(--fairway)"/>
          <stop offset="1" stop-color="var(--fairway-deep)"/>
        </linearGradient>
      </defs>
      <rect width="772" height="1100" fill="url(#sky-to-course)"/>
    </svg>

    <header class="headline">
      <p class="edition">3<sup>rd</sup> Annual</p>
      <h1 class="honoree">Marisol Quinn<br>Dorsey<br>Memorial</h1>
      <p class="sport">Golf</p>
      <p class="event">Tournament</p>
      <p class="format">4 person scramble</p>
    </header>

    <section class="schedule">
      <p class="date">Saturday<br>October<br>5<sup>th</sup> 2013</p>
      <p class="details">Fernhollow<br>Golf Club,<br>Auburn, IL<br>9:30 Registration<br>Shotgun<br>start at noon</p>
    </section>

    <footer class="fine-print">
      <p>Scholarships to Cedar Ridge High School seniors are made possible by our organization through this fundraiser.</p>
      <p>To Register go online to www.marisolqdorseygolf.teeupsignups.example or email marisoldorseyscholarship@mailbox.example</p>
    </footer>
  </main>
</body>
</html>
```